Webdesign für Metallbau-Wasserkraft Tessmar Lauber GmbH & Co. KG
Zielgruppe
Das Unternehmen ist im Metall- und Stahlwasserbau tätig. Die Haupkompetenz liegt im Stahlwasserbau, Rechenreinigung und Stahlbau tätig.
Aufgabenstellung
Die vorhandenen Seite https://www.metallbau-tessmar-lauber-beispiel.de/ soll einen Relaunch erhalten. Das Design soll frisch, modern und aussagekräftig erscheinen, trotz der Tradition und des Handwerksbetriebes.
Die Navigationstruktur soll erhalten bleiben. Hinzu kommt der Punkt 'Neuigkeiten'.

```html
<!DOCTYPE html>
<html lang="de">
<head>
<meta charset="utf-8">
<title>Metallbau-Wasserkraft Tessmar Lauber GmbH &amp; Co. KG</title>
<link href="https://fonts.googleapis.com/css2?family=Rubik:wght@500;600;700&family=Work+Sans:wght@400;500;600;700&display=swap" rel="stylesheet">
<style>
:root{
  --navy:#004a69;
  --navy-dark:#003f5c;
  --ink:#2a3340;
  --text:#4a5568;
  --blue:#0b7bb8;
  --pill:#1f2d3d;
  --panel:#f2f2f2;
  --line:#dcdcdc;
  --white:#ffffff;
}
*{box-sizing:border-box;margin:0;padding:0}
html,body{width:1200px;height:4661px;overflow:hidden}
body{position:relative;background:var(--white);font-family:"Work Sans",sans-serif;color:var(--text)}
.abs{position:absolute}
h1,h2,h3,.year{font-family:"Rubik",sans-serif;color:var(--ink)}

/* header */
.site-header{left:0;top:0;width:1200px;height:67px;background:rgba(255,255,255,.92);z-index:3}
.brand-mark{left:24px;top:18px;width:32px;height:32px;background:var(--blue);border-radius:3px}
.main-nav a{position:absolute;top:22px;font-size:15px;color:var(--ink);text-decoration:none}
.nav-cta{left:1052px;top:13px;width:108px;height:30px;border-radius:15px;background:var(--blue);color:#fff;font-weight:700;font-size:15px;display:flex;align-items:center;justify-content:center}

/* hero */
.hero{left:0;top:0;width:1200px;height:708px;background:linear-gradient(100deg,#eef1f0 0%,#dfe4df 30%,#8f9c85 55%,#566a4c 75%,#3f5236 100%)}
.hero-title{left:94px;top:200px;font-size:49px;line-height:59px;font-weight:700;color:var(--ink)}

/* timeline */
.tl-card{background:#fff;box-shadow:0 4px 14px rgba(0,0,0,.12);padding:26px 22px 0 24px}
.year{font-size:54px;font-weight:600;line-height:1}
.tl-text{margin-top:14px;border-left:5px solid var(--navy);padding-left:11px;font-size:14.5px;line-height:17.5px;color:#5b6675;max-width:205px}
.tl-line{left:103px;top:1168px;width:985px;height:2px;background:var(--ink)}
.tl-dot{width:26px;height:26px;border-radius:50%;background:var(--navy);top:1156px}

/* heute */
.heute{left:434px;top:1262px;width:661px;height:503px;background:#fff;box-shadow:0 4px 16px rgba(0,0,0,.12);z-index:2;padding:26px 28px 0 30px;text-align:right}
.heute h2{font-size:58px;font-weight:500;line-height:1;margin-right:2px}
.heute-body{margin-top:8px;border-right:5px solid var(--navy);padding-right:12px;font-size:14.5px;line-height:17.5px;color:#5b6675}
.heute-body p{margin-bottom:16px}
.heute-body p.intro{max-width:500px;margin-left:auto}
.heute-body strong{display:block;font-weight:700;color:var(--navy);margin-bottom:18px}

.photo-weir{left:92px;top:1624px;width:826px;height:557px;background:linear-gradient(180deg,#6f9bd0 0%,#a9c4e2 40%,#c7cfc4 55%,#8a9a8a 75%,#3c4a52 100%)}
.zukunft{left:241px;top:2110px;width:751px;height:261px;background:var(--navy);z-index:2;padding:30px 34px}
.zukunft h2{color:#fff;font-size:58px;font-weight:500;line-height:1}
.zukunft-body{margin-top:14px;border-left:5px solid #fff;padding-left:11px;font-size:14.5px;line-height:17.5px;color:#fff;max-width:625px}

/* kunden */
.section-title{left:0;width:1200px;text-align:center;font-size:29px;font-weight:600}
.client{width:265px;height:66px;border-radius:10px;background:var(--blue);color:#fff;font-weight:700;font-size:15.5px;display:flex;align-items:center;justify-content:center}
.private{left:560px;top:2818px;width:472px;text-align:right;font-size:26px;line-height:30px;color:var(--ink)}
.lead{left:300px;top:3117px;width:600px;text-align:center;font-size:16px;line-height:19px;color:var(--ink)}

/* partner */
.partner{width:265px;height:235px;background:#fff;border-radius:10px;box-shadow:0 3px 12px rgba(0,0,0,.18);text-align:center}
.partner-logo{position:absolute;left:26px;top:24px;width:213px;height:64px;display:flex;align-items:center;justify-content:center;gap:14px;font-size:18px;color:#6b6f75;line-height:21px}
.partner-logo span.sq{width:40px;height:40px;background:#7d8288;flex:none}
.partner-name{position:absolute;left:0;top:124px;width:100%;font-weight:700;font-size:15.5px;color:var(--ink)}
.partner-btn{position:absolute;left:60px;top:168px;width:145px;height:42px;border-radius:21px;background:var(--pill);color:#fff;font-weight:600;font-size:15px;display:flex;align-items:center;justify-content:center}

/* contact */
.contact{left:40px;top:3636px;width:1118px;height:523px;background:var(--panel);border-radius:22px}
.contact-sub{left:380px;top:3732px;width:440px;text-align:center;font-size:16px;line-height:19px;color:var(--ink)}
.field{background:#fff;border:1px solid var(--line);font-size:14px;color:#9aa3ad;padding:7px 6px}
.field em{color:#c0262d;font-style:normal}
.select-dot{position:absolute;right:6px;top:9px;width:13px;height:13px;border-radius:50%;background:var(--ink)}
.required{left:373px;top:4030px;font-size:12px;color:#6b7280}
.required em{color:#c0262d;font-style:normal}
.send{left:501px;top:4067px;width:198px;height:44px;border-radius:22px;background:var(--navy);color:#fff;font-weight:600;font-size:15px;display:flex;align-items:center;justify-content:center}

/* footer */
.f-label{left:80px;font-size:13px;font-weight:600;letter-spacing:.5px;color:var(--blue)}
.f-value{left:181px;font-size:16px;color:var(--ink)}
.f-brand{left:78px;top:4500px;display:flex;align-items:center;gap:10px;font-size:14px;font-weight:400;color:var(--ink)}
.f-brand span.sq{width:36px;height:36px;background:var(--blue);flex:none}
.f-link{right:80px;font-size:13px;font-weight:600;letter-spacing:.5px;color:var(--blue);text-align:right}
.bottom-bar{left:0;top:4605px;width:1200px;height:56px;background:var(--navy-dark);color:#fff;font-size:13px;padding:20px 0 0 67px}
</style>
</head>
<body>

<header class="abs site-header">
  <div class="abs brand-mark" aria-label="Metallbau-Wasserkraft Tessmar Lauber"></div>
  <nav class="main-nav">
    <a style="left:331px">Über uns</a>
    <a style="left:440px">Stahlwasserbau</a>
    <a style="left:599px">Rechenreiniger</a>
    <a style="left:749px">Stahlbauprodukte</a>
    <a style="left:923px">Neuigkeiten</a>
  </nav>
  <div class="abs nav-cta">Kontakt</div>
</header>

<section class="abs hero" role="img" aria-label="Luftaufnahme des Firmengeländes mit Werkhallen am Fluss"></section>
<h1 class="abs hero-title">Qualitativ hochwertiger<br>Stahlwasser- und Metallbau<br>seit mehr als 45 Jahren</h1>

<article class="abs tl-card" style="left:103px;top:820px;width:268px;height:223px">
  <div class="year">1977</div>
  <p class="tl-text">als Familienunternehmen gegründet, beschäftigte sich unser Betrieb anfangs vor allem mit dem Bau von Kommunal-Schneepflügen.</p>
</article>
<article class="abs tl-card" style="left:389px;top:871px;width:268px;height:237px">
  <div class="year">1985</div>
  <p class="tl-text">Im Zuge der Instandsetzung unserer eigenen Wasserkraftanlage begannen wir, unsere Expertise auf den Stahlwasserbau zu verlagern.</p>
</article>
<article class="abs tl-card" style="left:677px;top:820px;width:268px;height:257px">
  <div class="year">1988</div>
  <p class="tl-text">Durch die ständige Erweiterung unseres Wissens und Könnens konnten wir uns in den Folgejahren als anerkannter Fachbetrieb im Raum Chemnitz etablieren.</p>
</article>

<div class="abs tl-line"></div>
<div class="abs tl-dot" style="left:130px"></div>
<div class="abs tl-dot" style="left:418px"></div>
<div class="abs tl-dot" style="left:707px"></div>
<svg class="abs" style="left:1000px;top:1138px" width="100" height="62" viewBox="0 0 100 62">
  <circle cx="32" cy="31" r="28" fill="none" stroke="var(--blue)" stroke-width="2"/>
  <circle cx="32" cy="31" r="22" fill="none" stroke="var(--navy)" stroke-width="3"/>
  <circle cx="32" cy="31" r="15" fill="var(--blue)"/>
  <polyline points="82,22 92,31 82,40" fill="none" stroke="var(--ink)" stroke-width="2.5"/>
</svg>

<article class="abs heute">
  <h2>Heute</h2>
  <div class="heute-body">
    <p class="intro">Heute haben wir unsere Fähigkeiten beim Bau von Schützanlagen, Rechenreinigern, Wehrklappen und Co. perfektioniert. Neben dem Stahlwasserbau umfasst unser Leistungsspektrum folgende Bereiche:</p>
    <strong>ALLGEMEINER STAHLBAU</strong>
    <strong>GELÄNDERBAU NACH GEL-VORSCHRIFTEN</strong>
    <strong style="margin-bottom:36px">BAU VON TOR- UND TREPPENANLAGEN</strong>
    <p>Auf ca. 1100 m2 Produktionsfläche sind wir täglich mit Fachverstand, Engagement und unter Zuhilfenahme modernster technischer Anlagen für die Realisierung Ihres Projekts im Einsatz. Maßgeblich für unseren Erfolg ist unser hervorragend ausgebildetes Team, zu dem unter anderem zwei Handwerksmeister, ein Schweißingenieur und zwei Techniker zählen. Zufriedene Kunden aus ganz Deutschland sind der beste Nachweis unserer Kompetenz und Einsatzfreude.</p>
    <strong style="margin-bottom:0">Wir sind zertifiziert EXC3 nach EN 1090-2.</strong>
  </div>
</article>

<div class="abs photo-weir" role="img" aria-label="Wehranlage mit Stahlgeländern und Treppen an einem Fluss"></div>
<article class="abs zukunft">
  <h2>Unsere Zukunft</h2>
  <p class="zukunft-body">Die Zufriedenheit unserer Kunden treibt uns an. Um das Niveau unserer Fertigungsqualität auch in den kommenden Jahren stetig zu steigern, nutzen wir vielfältige Weiter- und Fortbildungsangebote.<br>Die intensive und enge Zusammenarbeit mit unseren Kunden nutzen wir, um Markttendenzen früh zu erkennen und neue Wege zu gehen.</p>
</article>

<h2 class="abs section-title" style="top:2540px">Unsere Kunden</h2>
<div class="abs client" style="left:167px;top:2619px">Talsperrenverwaltungen</div>
<div class="abs client" style="left:467px;top:2619px">Flussmeistereien</div>
<div class="abs client" style="left:766px;top:2619px">Bauunternehmen</div>
<div class="abs client" style="left:167px;top:2710px">Energieversorger</div>
<div class="abs client" style="left:467px;top:2710px">Wasserkraftbetreiber</div>
<div class="abs client" style="left:766px;top:2710px">Fischzuchtbetreiber</div>
<p class="abs private">...und Privatkunden aus Chemnitz,<br>Sachsen und ganz Deutschland.</p>

<h2 class="abs section-title" style="top:3065px">Unsere Partner</h2>
<p class="abs lead">Um den Anforderungen unserer Kunden zu jeder Zeit kompromisslos gerecht werden zu können, setzen wir auf die Zusammenarbeit mit versierten Partnerbetrieben unseres Vertrauens.</p>

<article class="abs partner" style="left:167px;top:3231px">
  <div class="partner-logo"><span>Henrik Solberg<br>Baugeschäft</span><span class="sq"></span></div>
  <div class="partner-name">Henrik Solberg Baugeschäft</div>
  <div class="partner-btn">Kontakt</div>
</article>
<article class="abs partner" style="left:467px;top:3231px">
  <div class="partner-logo"><span>Henrik Solberg<br>Baugeschäft</span><span class="sq"></span></div>
  <div class="partner-name">Henrik Solberg Baugeschäft</div>
  <div class="partner-btn">Kontakt</div>
</article>
<article class="abs partner" style="left:766px;top:3231px">
  <div class="partner-logo"><span>Henrik Solberg<br>Baugeschäft</span><span class="sq"></span></div>
  <div class="partner-name">Henrik Solberg Baugeschäft</div>
  <div class="partner-btn">Kontakt</div>
</article>

<section class="abs contact"></section>
<h2 class="abs section-title" style="top:3684px;font-size:31px">Was können wir für Sie tun?</h2>
<p class="abs contact-sub">Unser Team freut sich auf Ihre Anfrage, wir sind jederzeit für Sie da.</p>
<div class="abs field" style="left:373px;top:3808px;width:212px;height:31px">Name<em>*</em></div>
<div class="abs field" style="left:614px;top:3808px;width:211px;height:31px">Email<em>*</em></div>
<div class="abs field" style="left:373px;top:3859px;width:212px;height:31px">Grund / Anliegen<em>*</em><span class="select-dot"></span></div>
<div class="abs field" style="left:614px;top:3859px;width:211px;height:31px">Telefon</div>
<div class="abs field" style="left:373px;top:3910px;width:452px;height:110px">Nachricht</div>
<div class="abs required"><em>*</em> Pflichtfelder</div>
<div class="abs send">Nachricht senden</div>

<footer>
  <div class="abs f-label" style="top:4339px">ADRESSE:</div>
  <div class="abs f-value" style="top:4336px">Lindenauer Weg 14 | 09999 Musterhain</div>
  <div class="abs f-label" style="top:4384px">TELEFON:</div>
  <div class="abs f-value" style="top:4381px">+49 (0) 30000 55512</div>
  <div class="abs f-label" style="top:4430px">EMAIL:</div>
  <div class="abs f-value" style="top:4427px">info@metallbau-tessmar-lauber-beispiel.de</div>
  <div class="abs f-brand"><span class="sq"></span><span>Metallbau-Wasserkraft Tessmar Lauber</span></div>
  <div class="abs f-link" style="top:4339px">KONTAKT</div>
  <div class="abs f-link" style="top:4377px">ANFAHRT</div>
  <div class="abs f-link" style="top:4416px">IMPRESSUM</div>
  <div class="abs f-link" style="top:4454px">DATENSCHUTZ</div>
  <div class="abs f-link" style="top:4493px">SITEMAP</div>
  <div class="abs bottom-bar">© 2024 Metallbau-Wasserkraft Tessmar Lauber GmbH &amp; Co. KG</div>
</footer>

</body>
</html>
```